Finance web application design

We need a design for a new responsive finance web application. It should look uber professional and modern.

Inspiration and design we like:

website:
http://www.halverstone.com/

The application presented here:
http://financial.marrowgate.com/en/products/tools-applications/trading-investment-tools/vexla-trading-software.html

https://apps.pindlewick.com/us/app/kestrovan-for-tabrix/id582019346?mt=8

The application presented here (Tabrix version):
https://apps.pindlewick.com/en/app/zumik-forex-trading/id481033866?mt=8&utm_source=zumikButton

Target Market(s)

Private Investors

Industry/Entity Type

Finance

Number of Pages Required

5+ page

Font styles to use
Other font styles liked:
• Nobile

Requirements
Must have
• Colors for "up" changes: green
• Colors for "down" changes: red
• Fonts in tables must be very easy to read -
• Deliver design for all pages attached.
Nice to have
• A dark (gray) background
• Graphs should be shaded and partly transparent - orange or blue
• White text as "normal" - orange text / blue text for headers
Should not have
• White background

```html
<!DOCTYPE html>
<html lang="en">
<head>
<meta charset="utf-8">
<title>Finance – Home</title>
<link href="https://fonts.googleapis.com/css2?family=Source+Sans+3:wght@400;600;700&display=swap" rel="stylesheet">
<style>
:root{
  --canvas:#ffffff;
  --header-grey:#a7a7a7;
  --brand-green:#5bb600;
  --brand-red:#cc0a22;
  --light-grey:#e0e0e0;
  --mid-grey:#a9a9a9;
  --card-grey:#d3d3d3;
  --ink:#2b2b2b;
  --ink-soft:#4a4a4a;
  --white:#ffffff;
  --navy:#1d2a4a;
  --chart-bg:#17171c;
  --chart-purple:#a04ad8;
  --chart-orange:#e0a020;
  --icon-light:#e4e4e4;
  --icon-mid:#a8a8a8;
  --icon-dark:#6e6e6e;
}
*{margin:0;padding:0;box-sizing:border-box}
html,body{width:1200px;height:900px;overflow:hidden;background:var(--canvas)}
body{font-family:"Source Sans 3",Arial,sans-serif;color:var(--ink)}
.page{position:absolute;left:379px;top:0;width:442px;height:900px;overflow:hidden}
.abs{position:absolute}

.site-header{left:0;top:0;width:442px;height:68px;background:var(--header-grey)}
.logo-mark{left:34px;top:19px;width:28px;height:28px;border-radius:50%;background:var(--brand-green)}
.logo-name{left:70px;top:36px;font-size:11px;font-weight:600;color:var(--navy);line-height:1}
.search{left:335px;top:26px;width:74px;height:12px;border:1px solid #d8d8d8;font-size:5px;color:#eee;padding:2px 3px;line-height:7px}
.search svg{position:absolute;right:3px;top:2px}

.main-nav{left:0;top:68px;width:442px;height:19px;background:var(--brand-green);list-style:none}
.main-nav li{position:absolute;top:4px;font-size:8.5px;font-weight:600;color:var(--white);transform:translateX(-50%);white-space:nowrap}

.hero{left:0;top:87px;width:442px;height:181px;background:linear-gradient(160deg,#b9b6ae 0%,#8a8780 40%,#5c5a55 75%,#9a9892 100%)}
.hero-title{left:0;top:74px;width:442px;text-align:center;font-size:17px;font-weight:600;line-height:17px;color:var(--white);text-shadow:0 1px 2px rgba(0,0,0,.5)}
.hero-arrow{top:73px;width:19px;height:36px;background:var(--brand-red)}
.hero-arrow.prev{left:0;border-radius:0 18px 18px 0}
.hero-arrow.next{right:0;border-radius:18px 0 0 18px}
.hero-arrow svg{position:absolute;top:11px}
.dots{left:368px;top:169px;display:flex;gap:3px}
.dots span{width:8px;height:8px;border-radius:50%;border:1.5px solid var(--brand-red);background:var(--white)}
.dots span.on{border-color:#e0a020;background:#fff3cf}
.hero-shadow{left:0;top:268px;width:442px;height:21px;background:linear-gradient(#8d8d8d,#c9c9c9)}

.about{left:0;top:289px;width:442px;height:115px;background:var(--brand-red);color:var(--white)}
.about h2{position:absolute;left:36px;top:9px;font-size:15px;font-weight:600}
.about p{position:absolute;left:36px;width:244px;font-size:6.6px;line-height:8.3px;font-weight:400}
.more{display:inline-block;background:#9a9a9a;color:#eee;padding:0 6px;margin-left:4px;line-height:8px}
.about-photo{left:286px;top:30px;width:118px;height:66px;background:linear-gradient(135deg,#3c4654,#8e9aa8 35%,#d9dee3 65%,#f1f3f5);box-shadow:2px 3px 5px rgba(0,0,0,.45)}
.band{left:0;top:404px;width:442px;height:10px;background:#9d9d9d}

.services{left:0;top:414px;width:442px;height:143px;background:var(--light-grey)}
.services h2{position:absolute;left:36px;top:8px;font-size:14px;font-weight:600;color:var(--brand-red)}
.service{position:absolute;top:36px;width:108px}
.service-icon{display:block;margin-left:28px}
.service h3{margin-top:3px;font-size:8px;font-weight:600;color:var(--brand-red);white-space:nowrap}
.service p{margin-top:2px;font-size:6.2px;line-height:10.2px;color:var(--ink)}

.features{left:0;top:557px;width:442px;height:162px;background:var(--mid-grey)}
.features h2{position:absolute;left:37px;top:9px;font-size:14px;font-weight:600;color:var(--white)}
.feature-card{position:absolute;top:34px;width:105px;height:105px;background:var(--card-grey);border:1px solid #ececec;box-shadow:2px 3px 4px rgba(0,0,0,.35);padding:4px 5px}
.feature-card h3{font-size:8px;font-weight:600;color:var(--brand-green)}
.feature-chart{display:block;margin-top:1px}
.feature-card p{margin-top:5px;font-size:5.9px;line-height:7.6px;color:var(--ink-soft);letter-spacing:-.05px}

.closing{left:0;top:719px;width:442px;height:137px;background:var(--light-grey)}
.closing h2{position:absolute;left:36px;top:12px;font-size:13px;font-weight:600;line-height:13px;color:#111}
.closing p{position:absolute;left:36px;top:42px;width:164px;font-size:6.6px;line-height:9.1px;color:var(--ink-soft)}
.closing-photo{left:231px;top:9px;width:173px;height:118px;border:1px solid #bbb;background:linear-gradient(135deg,#5d8fb8,#b8d3e8 35%,#f0f2f4 60%,#c9b48a 85%,#8a7450)}

.site-footer{left:0;top:856px;width:442px;height:44px;background:var(--brand-green)}
.footer-links{position:absolute;left:36px;top:21px;display:flex;gap:9px;list-style:none;font-size:4.6px;color:var(--white)}
.social{position:absolute;left:294px;top:20px;display:flex;gap:3px}
.social span{width:8px;height:8px;background:#eaeaea}
.footer-search{left:345px;top:18px;width:59px;height:11px;border:1px solid #cfe9b4;font-size:4.6px;color:#e3f3d2;padding:2px 3px}
</style>
</head>
<body>
<div class="page">

  <header class="site-header abs">
    <div class="logo-mark abs"></div>
    <div class="logo-name abs">Your Logo</div>
    <div class="search abs">Search
      <svg width="6" height="6" viewBox="0 0 6 6"><circle cx="2.5" cy="2.5" r="1.8" fill="none" stroke="#e5e5e5" stroke-width=".7"/><line x1="3.8" y1="3.8" x2="5.6" y2="5.6" stroke="#e5e5e5" stroke-width=".7"/></svg>
    </div>
  </header>

  <ul class="main-nav abs">
    <li style="left:43px">Home</li>
    <li style="left:93px">About us</li>
    <li style="left:147px">Services</li>
    <li style="left:201px">Investors</li>
    <li style="left:251px">News</li>
    <li style="left:296px">Careers</li>
    <li style="left:343px">Offices</li>
    <li style="left:393px">Contacts</li>
  </ul>

  <section class="hero abs" role="img" aria-label="Photo of a hand using a calculator and a phone over financial papers">
    <h1 class="hero-title abs">Lorem ipsum dolor sit amet,<br>consectetur adipiscing elit.</h1>
    <div class="hero-arrow prev abs"><svg style="left:4px" width="8" height="14" viewBox="0 0 8 14"><polyline points="7,1 1,7 7,13" fill="none" stroke="#fff" stroke-width="2"/></svg></div>
    <div class="hero-arrow next abs"><svg style="left:7px" width="8" height="14" viewBox="0 0 8 14"><polyline points="1,1 7,7 1,13" fill="none" stroke="#fff" stroke-width="2"/></svg></div>
    <div class="dots abs"><span class="on"></span><span></span><span></span><span></span></div>
  </section>
  <div class="hero-shadow abs"></div>

  <section class="about abs">
    <h2>About Us</h2>
    <p style="top:30px">Lorem ipsum dolor sit amet, consectetur adipiscing elit. Proin egestas a felis non volutpat. Fusce lectus risus, aliquet non fringilla vel, porttitor et mi. Suspendisse tincidunt augue convallis magna fringilla lacinia. Quisque at commodo purus. Donec pulvinar bibendum neque, eu ultricies mauris convallis vitae. Sed dignissim purus libero, pretium dapibus sem aliquam et.</p>
    <p style="top:79px">Quisque et leo porttitor, dictum lorem in, efficitur enim. Pellentesque dapibus ligula tempus dolor tincidunt dictum. <span class="more">More...</span></p>
    <div class="about-photo abs" role="img" aria-label="Photo of a business meeting desk with charts and a laptop"></div>
  </section>
  <div class="band abs"></div>

  <section class="services abs">
    <h2>Our services</h2>
    <div class="service" style="left:37px">
      <svg class="service-icon" width="38" height="40" viewBox="0 0 38 40" aria-label="Coin stack icon" role="img">
        <g stroke="var(--icon-dark)" stroke-width=".6">
          <rect x="4" y="18" width="14" height="20" fill="var(--icon-mid)"/><ellipse cx="11" cy="38" rx="7" ry="2" fill="var(--icon-mid)"/><ellipse cx="11" cy="18" rx="7" ry="2" fill="var(--icon-light)"/>
          <rect x="14" y="8" width="14" height="30" fill="var(--icon-mid)"/><ellipse cx="21" cy="38" rx="7" ry="2" fill="var(--icon-mid)"/><ellipse cx="21" cy="8" rx="7" ry="2" fill="var(--icon-light)"/>
          <rect x="22" y="20" width="14" height="18" fill="var(--icon-mid)"/><ellipse cx="29" cy="38" rx="7" ry="2" fill="var(--icon-mid)"/><ellipse cx="29" cy="20" rx="7" ry="2" fill="var(--icon-light)"/>
        </g>
        <g stroke="var(--icon-dark)" stroke-width=".4" fill="none">
          <path d="M14 12h14M14 16h14M14 20h14M14 24h14M14 28h14M14 32h14M4 22h14M4 26h14M4 30h14M4 34h14M22 24h14M22 28h14M22 32h14"/>
        </g>
      </svg>
      <h3>Lorem ipsum dolor sit amet.</h3>
      <p>Lorem ipsum dolor sit amet, consectetur adipiscing elit. Proin egestas a felis non volutpat. Fusce lectus risus, aliquet non fringilla vel, porttitor et mi.</p>
    </div>
    <div class="service" style="left:172px">
      <svg class="service-icon" width="30" height="40" viewBox="0 0 30 40" aria-label="Padlock icon" role="img">
        <path d="M8 18V11a7 7 0 0 1 14 0v7" fill="none" stroke="var(--icon-dark)" stroke-width="3"/>
        <rect x="3" y="17" width="24" height="21" rx="2" fill="var(--icon-mid)" stroke="var(--icon-dark)" stroke-width=".8"/>
        <rect x="4" y="18" width="10" height="19" fill="var(--icon-light)" opacity=".6"/>
        <circle cx="15" cy="26" r="2.2" fill="var(--icon-dark)"/><rect x="14.2" y="27" width="1.6" height="5" fill="var(--icon-dark)"/>
      </svg>
      <h3>Lorem ipsum dolor sit amet.</h3>
      <p>Lorem ipsum dolor sit amet, consectetur adipiscing elit. Proin egestas a felis non volutpat. Fusce lectus risus, aliquet non fringilla vel, porttitor et mi.</p>
    </div>
    <div class="service" style="left:300px">
      <svg class="service-icon" width="40" height="40" viewBox="0 0 40 40" aria-label="Rising arrow icon" role="img">
        <polyline points="2,37 12,26 18,31 30,14" fill="none" stroke="var(--icon-dark)" stroke-width="4" stroke-linejoin="round"/>
        <polygon points="24,10 36,6 33,18" fill="var(--icon-dark)"/>
        <polyline points="2,37 12,26 18,31 30,14" fill="none" stroke="var(--icon-light)" stroke-width="1.2" stroke-linejoin="round"/>
      </svg>
      <h3>Lorem ipsum dolor sit amet.</h3>
      <p>Lorem ipsum dolor sit amet, consectetur adipiscing elit. Proin egestas a felis non volutpat. Fusce lectus risus, aliquet non fringilla vel, porttitor et mi.</p>
    </div>
  </section>

  <section class="features abs">
    <h2>Features</h2>
    <article class="feature-card" style="left:37px">
      <h3>Search</h3>
      <svg class="feature-chart" width="94" height="39" viewBox="0 0 94 39" role="img" aria-label="Trading line chart">
        <rect width="94" height="39" fill="var(--chart-bg)"/>
        <rect x="2" y="2" width="18" height="1.5" fill="#777"/><rect x="2" y="6" width="12" height="3" fill="#ccc"/><rect x="2" y="31" width="12" height="2" fill="#ccc"/>
        <path d="M22 12h70M22 20h70M22 28h70" stroke="#333" stroke-width=".4"/>
        <path d="M22 30 L32 26 L40 28 L48 18 L56 22 L64 14 L72 20 L80 16 L92 22 L92 36 L22 36Z" fill="var(--chart-purple)" opacity=".35"/>
        <polyline points="22,30 32,26 40,28 48,18 56,22 64,14 72,20 80,16 92,22" fill="none" stroke="var(--chart-purple)" stroke-width=".9"/>
        <polyline points="22,24 30,22 38,25 46,20 54,26 62,22 70,27 78,24 92,28" fill="none" stroke="var(--chart-orange)" stroke-width=".7"/>
        <rect x="28" y="8" width="5" height="2" fill="var(--chart-purple)"/>
      </svg>
      <p>Lorem ipsum dolor sit amet, consectetur adipiscing elit. Proin egestas a felis non volutpat. Fusce lectus risus, aliquet non fringilla vel, porttitor et mi. Suspendisse tincidunt augue</p>
    </article>
    <article class="feature-card" style="left:169px">
      <h3>Alerts</h3>
      <svg class="feature-chart" width="94" height="39" viewBox="0 0 94 39" role="img" aria-label="Trading line chart">
        <rect width="94" height="39" fill="var(--chart-bg)"/>
        <rect x="2" y="2" width="18" height="1.5" fill="#777"/><rect x="2" y="6" width="12" height="3" fill="#ccc"/><rect x="2" y="31" width="12" height="2" fill="#ccc"/>
        <path d="M22 12h70M22 20h70M22 28h70" stroke="#333" stroke-width=".4"/>
        <path d="M22 28 L30 24 L38 27 L46 16 L54 21 L62 13 L70 19 L80 15 L92 20 L92 36 L22 36Z" fill="var(--chart-purple)" opacity=".35"/>
        <polyline points="22,28 30,24 38,27 46,16 54,21 62,13 70,19 80,15 92,20" fill="none" stroke="var(--chart-purple)" stroke-width=".9"/>
        <polyline points="22,25 30,21 38,26 46,22 54,27 62,21 70,26 78,23 92,27" fill="none" stroke="var(--chart-orange)" stroke-width=".7"/>
        <rect x="28" y="8" width="5" height="2" fill="var(--chart-purple)"/>
      </svg>
      <p>Lorem ipsum dolor sit amet, consectetur adipiscing elit. Proin egestas a felis non volutpat. Fusce lectus risus, aliquet non fringilla vel, porttitor et mi. Suspendisse tincidunt augue</p>
    </article>
    <article class="feature-card" style="left:300px">
      <h3>Trading</h3>
      <svg class="feature-chart" width="94" height="39" viewBox="0 0 94 39" role="img" aria-label="Trading line chart">
        <rect width="94" height="39" fill="var(--chart-bg)"/>
        <rect x="2" y="2" width="18" height="1.5" fill="#777"/><rect x="2" y="6" width="12" height="3" fill="#ccc"/><rect x="2" y="31" width="12" height="2" fill="#ccc"/>
        <path d="M22 12h70M22 20h70M22 28h70" stroke="#333" stroke-width=".4"/>
        <path d="M22 31 L32 25 L40 29 L48 17 L56 23 L64 15 L72 21 L82 14 L92 21 L92 36 L22 36Z" fill="var(--chart-purple)" opacity=".35"/>
        <polyline points="22,31 32,25 40,29 48,17 56,23 64,15 72,21 82,14 92,21" fill="none" stroke="var(--chart-purple)" stroke-width=".9"/>
        <polyline points="22,23 30,23 38,26 46,21 54,25 62,23 70,28 78,24 92,26" fill="none" stroke="var(--chart-orange)" stroke-width=".7"/>
        <rect x="28" y="8" width="5" height="2" fill="var(--chart-purple)"/>
      </svg>
      <p>Lorem ipsum dolor sit amet, consectetur adipiscing elit. Proin egestas a felis non volutpat. Fusce lectus risus, aliquet non fringilla vel, porttitor et mi. Suspendisse tincidunt augue</p>
    </article>
  </section>

  <section class="closing abs">
    <h2>Lorem ipsum dolor sit amet,<br>consectetur adipiscing elit.</h2>
    <p>Lorem ipsum dolor sit amet, consectetur adipiscing elit. Proin egestas a felis non volutpat. Fusce lectus risus, aliquet non fringilla vel, porttitor et mi. Suspendisse tincidunt augue convallis magna fringilla lacinia. Quisque at commodo purus. Donec pulvinar bibendum neque, eu ultricies mauris convallis vitae. Sed dignissim purus libero, pretium dapibus sem aliquam et.</p>
    <div class="closing-photo abs" role="img" aria-label="Photo of hands writing on financial reports beside a calculator and coins"></div>
  </section>

  <footer class="site-footer abs">
    <ul class="footer-links">
      <li>Cookie Policy</li><li>Privacy Statement</li><li>Terms of Use</li><li>Copyright Information</li><li>Site Map</li>
    </ul>
    <div class="social"><span></span><span></span><span></span><span></span></div>
    <div class="footer-search abs">Search Careers</div>
  </footer>

</div>
</body>
</html>
```